Small Business Consulting Firm Needs Business Card Design

Need a sleek modern business card with 2 sides matching the colors of our logo. We will be placing these with a mailer we are sending out. These business cards will only ever be given to business owners. We operate helping businesses who are struggling with cash flow or finances. If the green and blue design needs to be moved to the right of "Harborline Crest Consulting" for aesthetic purposes that is ok. We will need an editable file if possible. We would like to include the reps name, email, website, and phone number. For now just use Peter Vance, pvance@harborlinecrest.com, www.harborlinecrest.com, and 833-555-0172.

```html
<!DOCTYPE html>
<html lang="en">
<head>
<meta charset="utf-8">
<title>Harborline Crest Consulting – Business Card</title>
<link rel="stylesheet" href="https://fonts.googleapis.com/css2?family=Montserrat:wght@300;400&family=Lato:wght@400;700&display=swap">
<style>
  :root {
    --page-bg: #ededed;
    --card-dark: #2a2a2a;
    --card-light: #ffffff;
    --brand-green: #6db33f;
    --brand-blue: #1565b0;
    --brand-navy: #0e4a8a;
    --ink: #1c1c1c;
    --ink-soft: #3a3a3a;
    --white: #ffffff;
  }
  * { box-sizing: border-box; margin: 0; padding: 0; }
  html, body { width: 1200px; height: 757px; overflow: hidden; }
  body { background: var(--page-bg); position: relative; font-family: "Lato", sans-serif; }

  .card { position: absolute; top: 195px; width: 498px; height: 299px; overflow: hidden; }
  .card--front { left: 90px; background: var(--card-dark); }
  .card--back { left: 650px; background: var(--card-light); }

  .brand-mark { position: absolute; width: 54px; height: 54px; background: var(--brand-green); }
  .brand-name, .brand-tagline {
    position: absolute; font-family: "Montserrat", sans-serif; font-weight: 300;
    text-transform: uppercase; white-space: nowrap;
  }

  .card--front .brand-mark { left: 222px; top: 74px; }
  .card--front .brand-name { left: 0; right: 0; top: 164px; text-align: center; font-size: 24px; letter-spacing: 1px; color: var(--white); }
  .card--front .brand-tagline { left: 0; right: 0; top: 196px; text-align: center; font-size: 12px; letter-spacing: 5px; color: var(--white); }
  .website { position: absolute; left: 0; right: 0; top: 264px; text-align: center; font-weight: 700; font-size: 13.5px; letter-spacing: 0.6px; color: var(--brand-green); }

  .card--back .brand-mark { left: 352px; top: 22px; width: 48px; height: 48px; }
  .card--back .brand-name { right: 26px; top: 96px; font-size: 17px; letter-spacing: 0.8px; color: var(--ink-soft); }
  .card--back .brand-tagline { right: 26px; top: 117px; font-size: 10px; letter-spacing: 3.6px; color: var(--ink-soft); }

  .rep-name { position: absolute; left: 29px; top: 132px; font-size: 15px; color: var(--brand-blue); }
  .rep-title { position: absolute; left: 29px; top: 152px; font-size: 10px; font-weight: 700; color: var(--ink); }
  .contact-list { position: absolute; left: 29px; top: 180px; list-style: none; font-size: 11px; color: var(--ink); }
  .contact-list li { display: flex; align-items: center; gap: 8px; height: 18px; }
  .contact-list svg { width: 12px; height: 12px; fill: var(--brand-green); }
  .address { position: absolute; left: 29px; top: 220px; font-style: normal; font-weight: 700; font-size: 11.5px; line-height: 15px; color: var(--brand-navy); }

  .accent-band {
    position: absolute; left: 0; right: 0; bottom: 0; height: 26px;
    background: linear-gradient(to right, var(--brand-green) 0%, var(--brand-green) 45%, var(--brand-navy) 100%);
  }
</style>
</head>
<body>

<section class="card card--front" aria-label="Card front">
  <div class="brand-mark" aria-hidden="true"></div>
  <div class="brand-name">Harborline Crest</div>
  <div class="brand-tagline">Consulting</div>
  <div class="website">www.harborlinecrest.com</div>
</section>

<section class="card card--back" aria-label="Card back">
  <div class="brand-mark" aria-hidden="true"></div>
  <div class="brand-name">Harborline Crest</div>
  <div class="brand-tagline">Consulting</div>

  <div class="rep-name">Peter Vance</div>
  <div class="rep-title">Owner / Founder</div>

  <ul class="contact-list">
    <li>
      <svg viewBox="0 0 12 12" aria-hidden="true"><path d="M1 4 Q6 0 11 4 L9.5 5.5 L8 4.2 L4 4.2 L2.5 5.5 Z M3 6 H9 L10 11 H2 Z"/></svg>
      <span>(833) 555-0172</span>
    </li>
    <li>
      <svg viewBox="0 0 12 12" aria-hidden="true"><path d="M1 3 H11 V10 H1 Z M1.6 3.6 L6 7 L10.4 3.6" stroke="#fff" stroke-width="0.9"/></svg>
      <span>pvance@harborlinecrest.com</span>
    </li>
  </ul>

  <address class="address">1450 W Ridgeway Ave<br>Millbrook, Carden County 75412</address>

  <div class="accent-band" role="img" aria-label="Decorative green and blue brand band along the card's lower edge"></div>
</section>

</body>
</html>
```